Wealth management firm needs a business card design

Using my logo, create a business card that covers all of the regulatory wordings that I need. It must have - Registered Office 5-7 Pellinore Court, Edinburgh, EH9 2QW. Registered in Scotland under number SC738204. Corvell Wealth Management Ltd is an appointed representative of Quintor wealth management Ltd, which is authorised and regulated by the Monetary Standards Council.

Target Market(s)

professional clients

Industry/Entity Type

finance

Contact Information for Business Card

Corvell Wealth Management, Rupert Ashdown-Kerr, Director, 9 Tanner Row, Edinburgh, EH2 4NP. 07812 455 193, rupert.ashdown-kerr@corvellwealth.example , www.corvellwealth.example

Font styles to use
Serif

Colors
0054AA
0677BA
7BADD7
CADEEF
E8F1F8

Requirements
Must have
• regulatory wording in small text at bottom

```html
<!DOCTYPE html>
<html lang="en">
<head>
<meta charset="utf-8">
<title>Corvell Wealth Management – Business Card</title>
<link rel="stylesheet" href="https://fonts.googleapis.com/css2?family=Noto+Serif:wght@400;700&family=Tinos:wght@400&display=swap">
<style>
  :root {
    --stage: #222222;
    --ink: #1c1c1c;
    --ink-soft: #4a4a4a;
    --paper: #ffffff;
    --brand-deep: #0054AA;
    --brand: #3a6fb8;
    --brand-mid: #7BADD7;
    --brand-pale: #CADEEF;
    --brand-wash: #E8F1F8;
    --back-dark: #26272e;
    --back-pattern: #34353d;
    --on-dark: #ffffff;
  }
  * { box-sizing: border-box; margin: 0; padding: 0; }
  html, body { width: 1200px; height: 780px; overflow: hidden; }
  body {
    background: var(--stage);
    display: flex;
    align-items: center;
    justify-content: center;
    gap: 60px;
    font-family: "Tinos", "Times New Roman", serif;
  }
  .card {
    position: relative;
    width: 520px;
    height: 300px;
    overflow: hidden;
    border-radius: 2px;
  }

  /* Front */
  .card--front { background: var(--paper); color: var(--ink); }
  .wordmark {
    position: absolute;
    top: 22px; left: 34px;
    display: flex; align-items: center; gap: 12px;
  }
  .wordmark__text { text-align: right; }
  .wordmark__name {
    font-family: "Noto Serif", serif;
    font-size: 17px;
    font-weight: 400;
    color: var(--ink);
  }
  .wordmark__tagline {
    font-family: "Noto Serif", serif;
    font-size: 7.5px;
    color: var(--ink);
    margin-top: 2px;
  }
  .wordmark__dot {
    width: 40px; height: 40px;
    border-radius: 50%;
    background: var(--brand);
    flex: none;
  }
  .contact {
    position: absolute;
    top: 84px; left: 34px;
    font-size: 12.5px;
    line-height: 1.3;
  }
  .contact__address { margin-bottom: 8px; }
  .contact__list { list-style: none; }
  .contact__item { display: flex; align-items: center; gap: 7px; margin-bottom: 2px; }
  .contact__icon { width: 11px; height: 11px; flex: none; }
  .dot-field {
    position: absolute;
    right: 0; bottom: 0;
    width: 260px; height: 230px;
    background: radial-gradient(ellipse at 60% 55%, var(--brand-wash) 0%, rgba(232,241,248,0.55) 55%, rgba(255,255,255,0) 80%);
  }
  .person {
    position: absolute;
    right: 44px; top: 190px;
    text-align: right;
  }
  .person__name {
    font-family: "Noto Serif", serif;
    font-weight: 700;
    font-size: 22px;
    line-height: 1.2;
    color: var(--brand);
  }
  .person__role {
    font-family: "Tinos", serif;
    font-size: 14px;
    color: var(--ink);
    margin-top: 1px;
  }
  .corner-block {
    position: absolute;
    right: 0; top: 196px;
    width: 32px; height: 42px;
    background: var(--brand);
  }
  .regulatory {
    position: absolute;
    left: 34px; right: 44px; bottom: 12px;
    font-family: "Tinos", serif;
    font-size: 7px;
    line-height: 1.35;
    color: var(--ink-soft);
  }

  /* Back */
  .card--back { background: var(--back-dark); color: var(--on-dark); }
  .ring-pattern {
    position: absolute; inset: 0;
    background: linear-gradient(120deg, var(--back-dark) 0%, var(--back-pattern) 55%, #55565e 100%);
  }
  .back-mark {
    position: absolute; inset: 0;
    display: flex; flex-direction: column; align-items: center; justify-content: center;
  }
  .back-mark__row { display: flex; align-items: center; gap: 14px; }
  .back-mark__name {
    font-family: "Noto Serif", serif;
    font-size: 21px;
    color: var(--on-dark);
  }
  .back-mark__dot {
    width: 48px; height: 48px; border-radius: 50%;
    background: var(--brand);
  }
  .back-mark__tagline {
    font-family: "Noto Serif", serif;
    font-size: 9px;
    color: var(--on-dark);
    margin-top: 4px;
    margin-right: 62px;
  }
</style>
</head>
<body>
  <section class="card card--front" aria-label="Business card front">
    <div class="dot-field" role="img" aria-label="Pale blue scattered dot pattern"></div>

    <div class="wordmark">
      <div class="wordmark__text">
        <div class="wordmark__name">Corvell Wealth Management Ltd</div>
        <div class="wordmark__tagline">Personal Financial Advice</div>
      </div>
      <span class="wordmark__dot" aria-hidden="true"></span>
    </div>

    <div class="contact">
      <p class="contact__address">9 Tanner Row, Edinburgh,<br>EH2 4NP.</p>
      <ul class="contact__list">
        <li class="contact__item">
          <svg class="contact__icon" viewBox="0 0 12 12" aria-hidden="true"><path d="M3 1.2 L4.6 3.4 L3.8 4.6 Q5 7 7.4 8.2 L8.6 7.4 L10.8 9 L9.8 10.8 Q4.5 10.5 1.2 2.2 Z" fill="#3a6fb8"/></svg>
          <span>07812 455 193</span>
        </li>
        <li class="contact__item">
          <svg class="contact__icon" viewBox="0 0 12 12" aria-hidden="true"><circle cx="6" cy="6" r="5" fill="none" stroke="#3a6fb8" stroke-width="1.3"/><ellipse cx="6" cy="6" rx="2.2" ry="5" fill="none" stroke="#3a6fb8" stroke-width="1"/><line x1="1" y1="6" x2="11" y2="6" stroke="#3a6fb8" stroke-width="1"/></svg>
          <span>www.corvellwealth.example</span>
        </li>
        <li class="contact__item">
          <svg class="contact__icon" viewBox="0 0 12 12" aria-hidden="true"><rect x="1" y="2.5" width="10" height="7" rx="1" fill="#3a6fb8"/><path d="M1.5 3 L6 6.6 L10.5 3" fill="none" stroke="#fff" stroke-width="1"/></svg>
          <span>rupert.ashdown-kerr@corvellwealth.example</span>
        </li>
      </ul>
    </div>

    <span class="corner-block" aria-hidden="true"></span>

    <div class="person">
      <div class="person__name">Rupert Ashdown-Kerr</div>
      <div class="person__role">Director</div>
    </div>

    <p class="regulatory">Registered Office 5-7 Pellinore Court, Edinburgh, EH9 2QW. Registered in Scotland under number SC738204. Corvell Wealth Management Ltd is an appointed representative of Quintor wealth management Ltd, which is authorised and regulated by the Monetary Standards Council.</p>
  </section>

  <section class="card card--back" aria-label="Business card back">
    <div class="ring-pattern" role="img" aria-label="Dark repeating dotted ring pattern with a light sheen towards the right"></div>
    <div class="back-mark">
      <div class="back-mark__row">
        <span class="back-mark__name">Corvell Wealth Management Ltd</span>
        <span class="back-mark__dot" aria-hidden="true"></span>
      </div>
      <div class="back-mark__tagline">Personal Financial Advice</div>
    </div>
  </section>
</body>
</html>
```